14 and Wrens Bar and Grill Menu 2016

Our property is currently going through a renovation to modernize the look and feel of the unit. 14 and Wrens is a restaurant attached to a Dellaway branded hotel in WI and we are making changes as well to provide a gathering place for both guests inside and outside of the hotel.
We need a new menu layout to help attract the local market for our restaurant. We are going for hip and trendy, easy to read, with a layout that is different from the normal fold that is seen everywhere. I have included the logo
Attached is a menu we really like to help give an idea of our style

Target Market(s)

25-45yr old

Industry/Entity Type

American Restaurant

Font styles to use
Other font styles liked:
• Isabel Bold

Colors
1b1b1b
ec1f27
ffffff
d5d5d5

Requirements
Must have
• Must have multiple pages, bold fonts, and easy to change out pages if necessary
• photo on the front for a fun bar and grill type feel
• Menu included with page breaks
Nice to have
• bold headers for each category
• fun tag lines for each category
Should not have
• many pictures aside from the front and back pages of the menu

```html
<!DOCTYPE html>
<html lang="en">
<head>
<meta charset="utf-8">
<title>14 and Wrens Bar and Grill Menu</title>
<link href="https://fonts.googleapis.com/css2?family=Montserrat:wght@500;700;800&family=Nunito+Sans:wght@400;600&family=Oswald:wght@500&display=swap" rel="stylesheet">
<style>
  :root {
    --ink: #1b1b1b;
    --red: #ec1f27;
    --white: #ffffff;
    --grey: #d5d5d5;
  }
  * { box-sizing: border-box; margin: 0; padding: 0; }
  html, body { width: 816px; height: 1200px; overflow: hidden; background: var(--white); }
  .sheet { position: relative; width: 816px; height: 1200px; font-family: "Nunito Sans", sans-serif; color: var(--ink); font-size: 6.4px; line-height: 7.7px; }
  .abs { position: absolute; }

  .label { position: absolute; font-family: "Oswald", sans-serif; font-weight: 500; font-size: 17px; line-height: 20px; letter-spacing: .06em; color: var(--red); white-space: nowrap; }
  .label .tri { display: inline-block; width: 0; height: 0; border-left: 5px solid transparent; border-right: 5px solid transparent; border-top: 8px solid var(--red); margin: 0 8px 2px; }
  .label .tri-right { display: inline-block; width: 0; height: 0; border-top: 6px solid transparent; border-bottom: 6px solid transparent; border-left: 9px solid var(--red); margin-left: 6px; }

  .photo-back { left: 0; top: 46px; width: 406px; height: 540px; background: radial-gradient(ellipse at 45% 75%, #e6e6e6 0%, #9a9a9a 35%, #2a2a2a 70%, #111 100%); }
  .back-panel { left: 50px; top: 46px; width: 308px; height: 540px; background: rgba(205,205,205,.9); }
  .photo-front { left: 406px; top: 46px; width: 410px; height: 540px; background: radial-gradient(ellipse at 55% 65%, #8a8a8a 0%, #4a4a4a 30%, #1e1e1e 60%, #0b0b0b 100%); }
  .brand { left: 458px; top: 110px; width: 304px; text-align: center; font-family: "Montserrat", sans-serif; font-weight: 700; color: var(--white); font-size: 34px; line-height: 1.1; letter-spacing: .04em; }
  .menu-word { left: 606px; top: 246px; font-family: "Montserrat", sans-serif; font-weight: 500; font-size: 50px; line-height: 56px; color: var(--white); letter-spacing: .02em; }

  .photo-left { left: 0; top: 638px; width: 408px; height: 546px; background: linear-gradient(180deg, #e9e9e9 0%, #dcdcdc 55%, #bdbdbd 100%); }
  .photo-right { left: 408px; top: 638px; width: 408px; height: 546px; background: linear-gradient(180deg, #efefef 0%, #e2e2e2 60%, #c7c7c7 100%); }
  .edge-left { left: 0; top: 638px; width: 54px; height: 546px; background: linear-gradient(90deg, #8e8e8e, #b7b7b7); }
  .edge-right { left: 772px; top: 638px; width: 44px; height: 546px; background: linear-gradient(90deg, #b3b3b3, #8a8a8a); }

  .section-title { position: absolute; font-family: "Montserrat", sans-serif; font-weight: 800; font-size: 22px; line-height: 23px; letter-spacing: .05em; color: var(--red); text-align: center; }

  .item { position: absolute; text-align: center; }
  .item h4 { font-family: "Montserrat", sans-serif; font-weight: 700; font-size: 7.6px; line-height: 9px; letter-spacing: .08em; text-transform: uppercase; margin-bottom: 2px; white-space: nowrap; }
  .item p { font-size: 6.4px; line-height: 7.7px; }
  .price { display: block; color: var(--red); font-weight: 600; font-size: 7px; line-height: 9px; }
  .price.in { display: inline; line-height: inherit; }

  .note { font-family: "Montserrat", sans-serif; font-weight: 700; font-size: 8px; line-height: 11.6px; letter-spacing: .08em; text-align: center; text-transform: uppercase; }
  .rule { position: absolute; height: 1px; background: rgba(236,31,39,.45); }
  .extras { left: 50px; top: 444px; width: 308px; list-style: none; text-align: center; }
  .extras li { font-family: "Montserrat", sans-serif; font-weight: 700; font-size: 8.2px; letter-spacing: .1em; line-height: 14.6px; }
  .fine { font-size: 5.6px; line-height: 7px; font-style: italic; text-align: center; }
  .health { left: 446px; top: 1102px; width: 287px; height: 25px; border: 1px solid rgba(236,31,39,.5); font-size: 5.6px; line-height: 7.2px; font-style: italic; text-align: center; padding-top: 4px; }
</style>
</head>
<body>
<div class="sheet">

  <div class="label" style="left:126px; top:18px;"><span class="tri"></span>BACK COVER<span class="tri"></span></div>
  <div class="label" style="left:526px; top:18px;"><span class="tri"></span>FRONT COVER<span class="tri"></span></div>

  <!-- back cover -->
  <div class="abs photo-back" role="img" aria-label="Black and white photo of a pasta plate on a table"></div>
  <div class="abs back-panel"></div>
  <h2 class="section-title" style="left:50px; top:74px; width:308px;">ENTREES &amp;<br>PLATES</h2>

  <div class="item" style="left:58px; top:135px; width:144px;"><h4>Fish &amp; Chips</h4><p>beer-battered fish, tartar sauce, fries</p><span class="price">13.5</span></div>
  <div class="item" style="left:58px; top:170px; width:144px;"><h4>Tuscan Chicken Pasta</h4><p>grilled chicken, artichoke, cavatappi noodles, fresh spinach, three-cheese blend, basil, tomato, mushrooms, alfredo sauce</p><span class="price">13.5</span></div>
  <div class="item" style="left:58px; top:222px; width:144px;"><h4>Lemon Chicken</h4><p>lemon-parmesan breaded chicken, alfredo sauce, sautéed vegetables, herbed brown rice and quinoa</p><span class="price">12.5</span></div>
  <div class="item" style="left:58px; top:273px; width:144px;"><h4>Jambalaya</h4><p>sautéed chicken, andouille sausage, red pepper, celery, onion, house made creole sauce, brown rice</p><span class="price">15</span></div>
  <div class="item" style="left:58px; top:324px; width:144px;"><h4>Salmon</h4><p>herbed brown rice and quinoa,<br>sautéed vegetables</p><span class="price">18</span></div>

  <div class="item" style="left:206px; top:135px; width:148px;"><h4>Ribeye Steak</h4><p>canadian grill, garlic parmesan mashed potatoes, sautéed vegetables, fried onion strings</p><span class="price">15</span></div>
  <div class="item" style="left:206px; top:186px; width:148px;"><h4>Baby Back Ribs</h4><p>house smoked half rack, BBQ, garlic parmesan mashed potatoes sautéed vegetables</p><span class="price">15</span></div>
  <div class="item" style="left:206px; top:238px; width:148px;"><h4>Spicy Pasta</h4><p>shrimp, andouille sausage, cavatappi noodles, yellow onion, green and red pepper, garlic, chili sambal sauce, alfredo sauce, parmesan, parsley</p><span class="price">14</span></div>
  <div class="item" style="left:206px; top:297px; width:148px;"><h4>Baked Mac &amp; Cheese</h4><p>custom four cheese blend, macaroni, baked golden</p><span class="price">10.5</span>
    <p>+ broccoli, bacon or jalapeño <span class="price in">12</span><br>+ grilled or fried chicken <span class="price in">14</span><br>+ shrimp <span class="price in">15</span></p></div>

  <div class="rule" style="left:60px; top:373px; width:288px;"></div>
  <p class="note abs" style="left:60px; top:377px; width:288px;">Join us Fridays for all-you-can-eat fish fry, and<br>Sundays for our brunch buffet!</p>
  <h2 class="section-title" style="left:50px; top:412px; width:308px;">EXTRAS</h2>
  <ul class="abs extras">
    <li>HOUSE SALAD <span class="price in">4</span></li>
    <li>MAC &amp; CHEESE <span class="price in">4</span></li>
    <li>SEASONAL VEGGIES <span class="price in">4</span></li>
    <li>HOUSE MADE CHIPS <span class="price in">4</span></li>
    <li>BLACK BEANS <span class="price in">4</span></li>
    <li>RICE PILAF <span class="price in">4</span></li>
    <li>HOUSE SOUP <span class="price in">4</span></li>
  </ul>
  <p class="fine abs" style="left:60px; top:555px; width:288px;">An 18% service charge will be added to all purchases for parties of 8 or more.</p>

  <!-- front cover -->
  <div class="abs photo-front" role="img" aria-label="Black and white photo of a burger on a plate in a dim bar"></div>
  <div class="abs brand">14 AND WRENS<br>BAR AND GRILL</div>
  <div class="abs menu-word">MENU</div>

  <div class="label" style="left:138px; top:606px;"><span class="tri"></span>LEFT INTERIOR<span class="tri"></span></div>
  <div class="label" style="left:342px; top:606px;">FOLD<span class="tri-right"></span></div>
  <div class="label" style="left:516px; top:606px;"><span class="tri"></span>RIGHT INTERIOR<span class="tri"></span></div>

  <!-- left interior -->
  <div class="abs photo-left" role="img" aria-label="Faded photo of a plated dish on a wooden table"></div>
  <div class="abs edge-left"></div>
  <h2 class="section-title" style="left:54px; top:668px; width:354px;">APPETIZERS</h2>

  <div class="item" style="left:66px; top:702px; width:156px;"><h4>Bruschetta</h4><p>tomato, basil, garlic, olive oil &amp;<br>parmesan cheese on parmesan crostinis</p><p><span class="price in">9</span> | with shrimp <span class="price in">14</span></p></div>
  <div class="item" style="left:66px; top:746px; width:156px;"><h4>Spinach &amp; Artichoke Dip</h4><p>spinach, artichoke, parmesan &amp; garlic,<br>served with house-made, crispy tortilla chips</p><span class="price">9</span></div>
  <div class="item" style="left:66px; top:791px; width:156px;"><h4>Crunchy Chicken Fingers</h4><p>hand breaded &amp; deep fried</p><span class="price">10</span></div>
  <div class="item" style="left:66px; top:827px; width:156px;"><h4>Smoked Wings</h4><p>buffalo, barbecue, szechwan or fire<br>boneless <span class="price in">10</span> | traditional <span class="price in">11</span></p></div>

  <div class="item" style="left:226px; top:702px; width:168px;"><h4>Chicken Nachos</h4><p>grilled chicken, queso, black beans,<br>jalapeños, cilantro, pico de gallo,<br>guacamole, sour cream &amp; tortilla chips</p><span class="price">11</span></div>
  <div class="item" style="left:226px; top:755px; width:168px;"><h4>Roasted Vegetable Flatbread</h4><p>fresh spinach &amp; artichoke sauce, tomato,<br>mushrooms, basil, balsamic onions,<br>mozzarella &amp; provolone cheese blend</p><span class="price">11</span></div>
  <div class="item" style="left:226px; top:808px; width:168px;"><h4>Buffalo Chicken Flatbread</h4><p>grilled chicken, green onion, blue cheese crumbles,<br>buffalo sauce, smoked onion ranch,<br>mozzarella &amp; provolone cheese blend</p><span class="price">11.5</span></div>
  <div class="item" style="left:160px; top:866px; width:140px;"><h4>Fried Green Beans</h4><p>spicy, fried, sriracha mayo</p><span class="price">9</span></div>

  <h2 class="section-title" style="left:54px; top:901px; width:354px;">SALADS</h2>
  <div class="item" style="left:66px; top:932px; width:156px;"><h4>Pear &amp; Blue Cheese</h4><p>field greens, blue cheese crumbles, dried cranberries, candied pecans, balsamic glaze, served with an apple cider vinaigrette</p><span class="price">9</span></div>
  <div class="item" style="left:66px; top:983px; width:156px;"><h4>BLT Wedge</h4><p>iceberg lettuce, bacon, bruschetta, green onion,<br>egg, blue cheese crumbles, ranch</p><span class="price">9</span></div>
  <div class="item" style="left:66px; top:1026px; width:156px;"><h4>Classic Caesar</h4><p>romaine lettuce, parmesan cheese &amp; croutons</p><span class="price">8.5</span></div>
  <div class="item" style="left:226px; top:932px; width:168px;"><h4>Chop Salad</h4><p>iceberg lettuce, bacon, tomato, avocado,<br>carrot, blue cheese crumbles, onion, garbanzo<br>beans, egg, cucumber &amp; tortilla strips<br>served with our house vinaigrette</p><span class="price">9.5</span></div>
  <div class="item" style="left:226px; top:991px; width:168px;"><h4>Greek Salad</h4><p>romaine, tomatoes, cucumbers,<br>red onion, Kalamata olives,<br>pepperoncini peppers,<br>feta cheese, greek dressing</p><span class="price">9.5</span></div>

  <div class="rule" style="left:64px; top:1066px; width:326px;"></div>
  <div class="item" style="left:100px; top:1071px; width:260px;"><h4>Add on Protein Options</h4><p>chicken <span class="price in">4</span> | shrimp <span class="price in">5</span> | salmon <span class="price in">6</span></p></div>
  <h2 class="section-title" style="left:54px; top:1099px; width:354px;">SOUPS</h2>
  <p class="note abs" style="left:54px; top:1126px; width:354px;">Baked French Onion Soup <span class="price in">5</span><br>Chefs Choice Soup of the Day <span class="price in">4</span></p>

  <!-- right interior -->
  <div class="abs photo-right" role="img" aria-label="Faded photo of food on a rustic wooden board"></div>
  <div class="abs edge-right"></div>
  <h2 class="section-title" style="left:430px; top:668px; width:336px;">BURGERS &amp;<br>SANDWICHES</h2>
  <p class="abs" style="left:440px; top:724px; width:316px; text-align:center;">Served with your choice of tater tots, fries or chips | Substitute any of our extras for <span class="price in">$1</span><br>Try it as a chicken breast or black bean veggie burger for <span class="price in">$1.5</span></p>

  <div class="item" style="left:440px; top:754px; width:150px;"><h4>Bacon Burger</h4><p>cheddar cheese, barbecue sauce,<br>applewood smoked bacon,<br>&amp; fried onion strings*</p><span class="price">12</span></div>
  <div class="item" style="left:440px; top:806px; width:150px;"><h4>Southwest Burger</h4><p>pepper jack cheese, jalapeño &amp; avocado*</p><span class="price">12</span></div>
  <div class="item" style="left:440px; top:842px; width:150px;"><h4>Philly Burger</h4><p>mushrooms, onions &amp; provolone cheese*</p><span class="price">12</span></div>
  <div class="item" style="left:440px; top:877px; width:150px;"><h4>Hamburger</h4><p><span class="price in">9</span> | + cheese* <span class="price in">10</span></p></div>
  <div class="item" style="left:440px; top:910px; width:150px;"><h4>BBQ Pulled Pork</h4><p>smoked pulled pork, barbecue sauce, cheddar<br>cheese &amp; fried onion strings, on a brioche bun</p><span class="price">11.5</span></div>

  <div class="item" style="left:606px; top:754px; width:150px;"><h4>Turkey Club</h4><p>applewood smoked bacon, lettuce,<br>turkey, tomato, cheddar cheese &amp; mayo,<br>served on multi-grain bread</p><span class="price">12</span></div>
  <div class="item" style="left:606px; top:806px; width:150px;"><h4>Veggie Wrap</h4><p>sautéed carrots, red pepper, broccoli,<br>fresh spinach, avocado, queso fresco,<br>pesto mayo, balsamic glaze</p><span class="price">11</span></div>
  <div class="item" style="left:606px; top:858px; width:150px;"><h4>Crispy Chicken Melt</h4><p>beer-battered chicken breast, lettuce, tomato,<br>cheddar, sweet chili mayo, and brioche bun /<br>grilled or blackened available</p><span class="price">12</span></div>
  <div class="item" style="left:606px; top:909px; width:150px;"><h4>Reuben</h4><p>corned beef, sauerkraut, 1000 island, swiss,<br>marble rye bread</p><span class="price">12</span></div>

  <h2 class="section-title" style="left:430px; top:968px; width:336px;">LETTUCE WRAPS</h2>
  <div class="item" style="left:440px; top:1006px; width:150px;"><h4>Sesame Ginger<br>Lettuce Wraps</h4><p>green onion, yellow onion, red pepper, cilantro,<br>carrot, water chestnuts, ginger and soy sauce,<br>romaine lettuce cups, sweet thai chili<br>and dijon mustard sauces<br>chicken <span class="price in">12</span> | shrimp <span class="price in">14</span></p></div>
  <div class="item" style="left:602px; top:1006px; width:158px;"><h4>Jerk Chicken &amp; Shrimp<br>Lettuce Wraps</h4><p>Seared chicken and sautéed shrimp, jalapeño,<br>yellow onion, red pepper, carrot, pineapple,<br>cilantro, rice sticks, ginger and soy sauce, served<br>with romaine lettuce cups, barbecue and<br>chili sambal sauce</p><span class="price">12</span></div>

  <div class="abs health">*The State Department of Health wishes to inform you that eating undercooked meat, poultry or raw eggs<br>poses a health risk to anyone.</div>
  <p class="fine abs" style="left:446px; top:1147px; width:287px;">An 18% service charge will be added to all purchases for parties of 8 or more.</p>

</div>
</body>
</html>
```